New Business Card Design Project

Hi there

Could you please make a design that is soft and appealing to people who would purchase gemstones, buy healing jewellery, seek counselling, may seek energy healing and/or learn English. Essentially I'm looking for something with a soft human design. Please incorporate the logo and select font that can be easily read and softer images in the background - but not too busy. I would like it double sided as well.

Optional: Elements could include gemstones, feathers, plants and images that are happy and calming.

Target Market(s)

People into alternative health, those from non-English speaking backgrounds, businesses

Contact Information for Business Card

Lena Whitford
Mobile: 0418 265 093, Friendbook and Picturely Logos,
ABN: 61 472 185 034 (Australian Business Number - small at the bottom)

Requirements
Must have
• My project must have:
- Meadow Thread logo
- Symbols that represent the 4 main services: 1. Gemstones/jewellery, 2. counselling, 3. meditation/energy healing, 4. education
Nice to have
• Clear and easy to read.

```html
<!DOCTYPE html>
<html lang="en">
<head>
<meta charset="utf-8">
<title>Meadow Thread – Business Card</title>
<link rel="stylesheet" href="https://fonts.googleapis.com/css2?family=Arimo:wght@400;700&display=swap">
<style>
  :root {
    --backdrop: #2a2a2a;
    --backdrop-deep: #141414;
    --card: #0b0b0b;
    --card-edge: #1c1c1c;
    --leaf-green: #5aa825;
    --teal: #1fa59a;
    --soft-white: #e6e6e6;
    --icon-grey: #b3b3b3;
    --label-grey: #d0d0d0;
  }
  * { box-sizing: border-box; margin: 0; padding: 0; }
  html, body {
    width: 1200px; height: 900px; overflow: hidden;
    font-family: "Arimo", Arial, sans-serif;
  }
  .canvas {
    position: relative; width: 1200px; height: 900px;
    background: radial-gradient(ellipse at 50% 40%, var(--backdrop) 0%, var(--backdrop-deep) 100%);
    display: flex; align-items: center; justify-content: center; gap: 40px;
  }
  .card {
    position: relative; width: 540px; height: 310px;
    background: linear-gradient(160deg, var(--card-edge) 0%, var(--card) 45%, var(--card) 100%);
    border-radius: 22px;
    box-shadow: 0 18px 40px rgba(0,0,0,.55);
    overflow: hidden;
  }

  /* Front */
  .brand {
    position: absolute; top: 64px; left: 0; right: 0;
    display: flex; flex-direction: column; align-items: center; gap: 14px;
  }
  .brand-circle {
    width: 62px; height: 62px; border-radius: 50%;
    border: 3px solid var(--teal);
  }
  .brand-name {
    font-size: 34px; font-weight: 400; letter-spacing: 3px;
    color: var(--leaf-green); text-transform: uppercase;
  }
  .holder {
    position: absolute; left: 40px; bottom: 40px;
  }
  .holder-name {
    font-size: 26px; font-weight: 700; color: var(--leaf-green);
    text-transform: uppercase; letter-spacing: .5px;
  }
  .holder-phone {
    margin-top: 6px; font-size: 24px; color: var(--soft-white);
  }
  .details {
    position: absolute; right: 34px; bottom: 42px; text-align: right;
  }
  .social {
    display: flex; justify-content: flex-end; gap: 12px;
    font-size: 12px; color: var(--soft-white); margin-bottom: 8px;
  }
  .abn { font-size: 13px; color: var(--soft-white); }
  .abn-label { color: var(--teal); }

  /* Back */
  .services-title {
    position: absolute; top: 48px; left: 0; right: 0; text-align: center;
    font-size: 24px; font-weight: 700; color: var(--soft-white); letter-spacing: 1px;
  }
  .services {
    position: absolute; top: 118px; left: 30px; right: 30px;
    display: flex; justify-content: space-between; list-style: none;
  }
  .service {
    width: 110px; display: flex; flex-direction: column; align-items: center; gap: 14px;
  }
  .service-icon {
    width: 100px; height: 100px; border-radius: 50%;
    background: radial-gradient(circle at 40% 35%, #c4c4c4, var(--icon-grey));
  }
  .service-label { font-size: 14px; color: var(--label-grey); }
</style>
</head>
<body>
<main class="canvas">
  <section class="card card-front">
    <div class="brand">
      <span class="brand-circle"></span>
      <span class="brand-name">Meadow Thread</span>
    </div>
    <div class="holder">
      <p class="holder-name">Lena Whitford</p>
      <p class="holder-phone">0418 265 093</p>
    </div>
    <div class="details">
      <p class="social"><span>Picturely</span><span>Friendbook</span></p>
      <p class="abn"><span class="abn-label">ABN:</span> 61 472 185 034</p>
    </div>
  </section>

  <section class="card card-back">
    <h2 class="services-title">SERVICES</h2>
    <ul class="services">
      <li class="service">
        <span class="service-icon" role="img" aria-label="Counselling symbol: head silhouette with brain"></span>
        <span class="service-label">Counselling</span>
      </li>
      <li class="service">
        <span class="service-icon" role="img" aria-label="Education symbol: graduation cap"></span>
        <span class="service-label">Education</span>
      </li>
      <li class="service">
        <span class="service-icon" role="img" aria-label="Gemstones symbol: cut diamond"></span>
        <span class="service-label">Gemstones</span>
      </li>
      <li class="service">
        <span class="service-icon" role="img" aria-label="Meditation symbol: seated meditating figure"></span>
        <span class="service-label">Meditation</span>
      </li>
    </ul>
  </section>
</main>
</body>
</html>
```